Web-site for software development company

Full company name is “Quill Byte”. It is a software development company based in Russia. We provide IT and have extensive experience in a programming and in the business process outsourcing field including banking and financial services.

Design should be modern, strict, not too colorful and bright.
We need to analogous web-site like our partner has http://www.movalentech.example/home/
You can use text from this one.

The design must include 5 pages with the images (and their source files) for:
-Home
-Services
-About us
-Careers
-Contact us. There should be contacts, map with company address.

Industry/Entity Type

Software

Number of Pages Required

5+ page

Font styles to use
Serif
Sans Serif

Requirements
Must have
• Wordpress layout
• Web-design
• PSD-to-HTML job
• PSD sources should be delivered
Nice to have
• Colors like on partner`s web-site http://www.movalentech.example/home/

```html
<!DOCTYPE html>
<html lang="en">
<head>
<meta charset="utf-8">
<title>Quill Byte — Home</title>
<link href="https://fonts.googleapis.com/css2?family=Open+Sans:wght@400;600&display=swap" rel="stylesheet">
<style>
  :root {
    --page-bg: #f1f1f1;
    --panel-bg: #ffffff;
    --brand-blue: #2e3192;
    --nav-text: #4a4a4a;
    --heading: #3a3a3a;
    --body-text: #666666;
    --caption-light: rgba(128, 132, 196, 0.9);
    --caption-dark: rgba(55, 55, 55, 0.85);
    --phone-icon-bg: #b5b5b5;
    --phone-text-bg: rgba(205, 205, 205, 0.92);
    --social-bg: #24277a;
  }
  * { margin: 0; padding: 0; box-sizing: border-box; }
  html, body { width: 1200px; height: 1174px; overflow: hidden; }
  body {
    background: var(--page-bg);
    font-family: "Open Sans", Arial, sans-serif;
    position: relative;
  }
  .page {
    position: absolute; left: 99px; top: 17px; width: 1003px; height: 1129px;
    background: var(--panel-bg);
  }
  .brand {
    position: absolute; left: 14px; top: 35px;
    font-size: 21px; line-height: 28px; font-weight: 400; color: var(--heading); letter-spacing: 0.3px;
  }
  .main-nav { position: absolute; top: 48px; left: 0; width: 100%; font-size: 12px; line-height: 16px; }
  .main-nav a {
    position: absolute; color: var(--nav-text); text-decoration: none; letter-spacing: 0.3px; white-space: nowrap;
  }
  .main-nav a.active { color: var(--brand-blue); }
  .hero {
    position: absolute; left: 12px; top: 86px; width: 977px; height: 463px;
    background: linear-gradient(100deg, #e4e9ef 0%, #c9d0da 30%, #dfe4ea 55%, #b9b2a8 80%, #9da3ad 100%);
  }
  .phone-badge { position: absolute; right: 27px; top: 0; display: flex; height: 43px; }
  .phone-icon { width: 43px; background: var(--phone-icon-bg); display: flex; align-items: center; justify-content: center; }
  .phone-number {
    background: var(--phone-text-bg); color: #fff; font-size: 15.5px; line-height: 43px; padding: 0 13px 0 8px;
  }
  .caption { position: absolute; right: 30px; color: #fff; font-size: 15.5px; font-weight: 600; padding: 0 12px; line-height: 42px; height: 42px; }
  .caption-top { top: 327px; width: 397px; background: var(--caption-light); text-align: right; }
  .caption-bottom { top: 370px; width: 256px; background: var(--caption-dark); text-align: right; }
  .slider-dots { position: absolute; right: 35px; top: 426px; display: flex; gap: 7px; }
  .slider-dots span { width: 12px; height: 12px; border-radius: 50%; border: 2px solid #fff; }
  .slider-dots span.current { background: #fff; }
  .welcome { position: absolute; top: 575px; left: 0; width: 100%; text-align: center; }
  .welcome h1 { font-size: 26px; font-weight: 400; color: var(--heading); letter-spacing: 0.3px; }
  .welcome p { margin: 12px auto 0; width: 680px; font-size: 16.5px; line-height: 21px; color: var(--heading); }
  .services { position: absolute; top: 713px; left: 12px; width: 977px; }
  .service { position: absolute; top: 0; width: 225px; text-align: center; }
  .service-image { height: 144px; }
  .service h2 { font-size: 14px; font-weight: 600; color: var(--heading); margin-top: 15px; }
  .service p { font-size: 12px; line-height: 17px; color: var(--body-text); margin-top: 14px; }
  .site-footer {
    position: absolute; left: 0; bottom: 0; width: 100%; height: 86px; background: var(--brand-blue); color: #fff;
  }
  .footer-nav { position: absolute; left: 25px; top: 22px; font-size: 11.5px; font-weight: 600; }
  .footer-nav a { color: #fff; text-decoration: none; }
  .footer-nav .sep { margin: 0 9px; }
  .copyright { position: absolute; left: 24px; top: 47px; font-size: 12.5px; }
  .social { position: absolute; right: 19px; top: 26px; display: flex; gap: 6px; }
  .social span { width: 35px; height: 35px; border-radius: 50%; background: var(--social-bg); display: block; }
</style>
</head>
<body>
<div class="page">
  <header>
    <div class="brand">QUILL BYTE</div>
    <nav class="main-nav">
      <a class="active" style="left:551px">HOME</a>
      <a style="left:626px">SERVICES</a>
      <a style="left:719px">ABOUT US</a>
      <a style="left:818px">CAREERS</a>
      <a style="left:909px">CONTACT US</a>
    </nav>
  </header>

  <section class="hero" role="img" aria-label="Photo of a confident businessman in a suit with colleagues meeting in a bright office behind him">
    <div class="phone-badge">
      <div class="phone-icon">
        <svg width="18" height="22" viewBox="0 0 18 22"><path d="M5 1 L8 6 L6 8 C6.5 11 8 14 10.5 16 L13 14.5 L16.5 18.5 L13.5 21 C7 20 2 12 2.5 4 Z" fill="#fff"/></svg>
      </div>
      <div class="phone-number">+38 - 512 - 4470</div>
    </div>
    <div class="caption caption-top">Suspendisse vel interdum lacus, sit amet varius</div>
    <div class="caption caption-bottom">augue. Pellentesque iaculis</div>
    <div class="slider-dots"><span class="current"></span><span></span><span></span><span></span></div>
  </section>

  <section class="welcome">
    <h1>Welcome To Our Site</h1>
    <p>Our solutions aim to provide high value by optimising cost of ownership of technology investments for customers.</p>
  </section>

  <section class="services">
    <article class="service" style="left:0">
      <div class="service-image" role="img" aria-label="Woman standing before a whiteboard sketch of innovation ideas" style="background:linear-gradient(135deg,#f2f2f2,#d9d9d9)"></div>
      <h2>Software Development</h2>
      <p>We offer a wide range of language and platform expertise including Kestrel, Corvo, Lumen / Flare / Scriptline, and more.</p>
    </article>
    <article class="service" style="left:250px">
      <div class="service-image" role="img" aria-label="Person touching a glowing blue database interface" style="background:linear-gradient(160deg,#3f7fd0,#9fc6ee 60%,#dbe8f6)"></div>
      <h2>Databases</h2>
      <p>From database design/architecture to programming and administration, we work with all major platforms including Orbis 9i and 10g, TideSQL, NorthSQL, Basalt, Quarrydb and more.</p>
    </article>
    <article class="service" style="left:499px">
      <div class="service-image" role="img" aria-label="Businessman behind transparent screens of charts and data" style="background:linear-gradient(135deg,#2c6e8e,#1f3c52 50%,#3a7fa0)"></div>
      <h2>System Administration</h2>
      <p>Our SysAdmins can deploy, configure and administer a range of server platforms including Solvane and RedKite Lynx distributions.</p>
    </article>
    <article class="service" style="left:749px">
      <div class="service-image" role="img" aria-label="Two colleagues reviewing work at a laptop" style="background:linear-gradient(135deg,#c9c2b6,#5a5f6c 60%,#2f3645)"></div>
      <h2>Q/A &amp; Testing</h2>
      <p>Our Q/A Engineers can develop test plans and put systems and processes through rigorous testing.</p>
    </article>
  </section>

  <footer class="site-footer">
    <nav class="footer-nav">
      <a>HOME</a><span class="sep">|</span><a>SERVICES</a><span class="sep">|</span><a>ABOUT US</a><span class="sep">|</span><a>CAREERS</a><span class="sep">|</span><a>CONTACT US</a>
    </nav>
    <div class="copyright">Copyright &copy;&nbsp; yoursite, All Rights Reserved</div>
    <div class="social" aria-label="Social links"><span></span><span></span><span></span></div>
  </footer>
</div>
</body>
</html>
```